Dietitian clinic needs a business card design

We need a business card design for a new dietitian group based in Singapore called "Brightpath and Bloom". We provide expert, personalised nutrition care to support a wide range of health needs, from chronic conditions to mindful eating. Our team also offers consulting, speaking, and tailored solutions for healthcare providers, organisations, and food services.

Target Market(s)

Adults

Industry/Entity Type

Healthcare

Contact Information for Business Card

Name, position, contact number, email, website address, our logo

Requirements
Nice to have
• Clean, professional but welcoming look

```html
<!DOCTYPE html>
<html lang="en">
<head>
<meta charset="utf-8">
<title>Brightpath and Bloom – Business Card</title>
<link rel="stylesheet" href="https://fonts.googleapis.com/css2?family=Montserrat:wght@400;500;600;700&display=swap">
<style>
  :root {
    --teal: #2a5f73;
    --teal-dark: #22505f;
    --white: #ffffff;
    --ink: #1c1c1c;
    --backdrop: #3a3a3c;
    --shade: #cfd3d6;
  }
  * { margin: 0; padding: 0; box-sizing: border-box; }
  html, body { width: 1200px; height: 1200px; overflow: hidden; }
  body {
    background: var(--backdrop);
    font-family: "Montserrat", sans-serif;
    position: relative;
  }
  .card {
    position: absolute;
    left: 220px;
    width: 760px;
    height: 434px;
    border-radius: 30px;
    overflow: hidden;
  }
  .card-front { top: 110px; background: var(--white); }
  .card-back { top: 650px; background: linear-gradient(160deg, #2e6579, var(--teal-dark)); }

  .brand {
    position: absolute;
    display: flex;
    align-items: center;
    gap: 14px;
    font-weight: 700;
    letter-spacing: 0.01em;
    white-space: nowrap;
  }
  .brand-dot { border-radius: 50%; flex: none; }
  .card-front .brand { left: 120px; top: 70px; color: var(--teal); font-size: 40px; }
  .card-front .brand-dot { width: 30px; height: 30px; border: 5px solid var(--teal); }
  .card-back .brand { left: 0; right: 0; top: 188px; justify-content: center; color: var(--white); font-size: 46px; }
  .card-back .brand-dot { width: 34px; height: 34px; border: 6px solid var(--white); }

  .person { position: absolute; left: 70px; top: 208px; color: var(--teal); }
  .person-name { font-size: 34px; font-weight: 700; letter-spacing: 0.04em; }
  .person-title { font-size: 20px; font-weight: 500; color: var(--ink); letter-spacing: 0.06em; margin-top: 2px; }

  .divider { position: absolute; left: 70px; right: 60px; top: 292px; height: 1.5px; background: var(--teal); }

  .contact { position: absolute; left: 70px; top: 312px; font-size: 20px; color: var(--ink); }
  .contact li { list-style: none; display: flex; align-items: center; gap: 14px; height: 38px; }
  .contact svg { width: 22px; height: 22px; fill: var(--teal); flex: none; }

  .address { position: absolute; right: 60px; top: 222px; font-size: 17px; color: var(--ink); display: flex; gap: 12px; align-items: center; line-height: 1.3; }
  .address svg { width: 20px; height: 26px; fill: var(--teal); flex: none; }

  .band { position: absolute; left: 0; bottom: 0; width: 760px; height: 150px; }
  .website { position: absolute; right: 56px; bottom: 34px; color: var(--white); font-size: 19px; letter-spacing: 0.06em; }
</style>
</head>
<body>
  <section class="card card-front">
    <div class="brand"><span class="brand-dot"></span>Brightpath and Bloom</div>

    <div class="person">
      <div class="person-name">FULL NAME</div>
      <div class="person-title">TITLE</div>
    </div>

    <div class="address">
      <svg viewBox="0 0 20 26"><path d="M10 0C4.5 0 0 4.4 0 9.8 0 16.6 10 26 10 26s10-9.4 10-16.2C20 4.4 15.5 0 10 0zm0 13.8a4 4 0 1 1 0-8 4 4 0 0 1 0 8z"/></svg>
      <div>123 Name Street, 000<br>Your City, 00000-000</div>
    </div>

    <div class="divider"></div>

    <ul class="contact">
      <li><svg viewBox="0 0 24 24"><path d="M6.6 10.8a15.1 15.1 0 0 0 6.6 6.6l2.2-2.2c.3-.3.7-.4 1-.2 1.1.4 2.3.6 3.6.6.6 0 1 .4 1 1V20c0 .6-.4 1-1 1A17 17 0 0 1 3 4c0-.6.4-1 1-1h3.5c.6 0 1 .4 1 1 0 1.3.2 2.5.6 3.6.1.3 0 .7-.2 1z"/></svg>(000) 000 0000</li>
      <li><svg viewBox="0 0 24 24"><path d="M2 5h20v14H2zm2 2v.4l8 5.2 8-5.2V7zm0 2.8V17h16V9.8l-8 5.2z"/></svg>email@company.com</li>
    </ul>

    <svg class="band" viewBox="0 0 760 150" preserveAspectRatio="none">
      <path d="M0 150 V138 H330 C390 138 390 62 460 62 H760 V150 Z" fill="var(--shade)"/>
      <path d="M0 150 V146 H340 C400 146 400 70 470 70 H760 V150 Z" fill="var(--teal)"/>
    </svg>
    <div class="website">www.company.com</div>
  </section>

  <section class="card card-back">
    <div class="brand"><span class="brand-dot"></span>Brightpath and Bloom</div>
  </section>
</body>
</html>
```